"Brindle Oak Accupuncture" needs a Promotional Card - A6 size

Requirements
Must have
• Bright colours, pictures of happy people, acupuncture-related pictures.

```html
<!DOCTYPE html>
<html lang="en">
<head>
<meta charset="utf-8">
<title>Brindle Oak Accupuncture – Card Design</title>
<link href="https://fonts.googleapis.com/css2?family=Raleway:wght@300;400;500;700;800&display=swap" rel="stylesheet">
<style>
:root{
  --page:#e9e9e9;
  --bar-top:#f7f7f7;
  --bar-bottom:#d9d9d9;
  --ink:#1f1f1f;
  --red:#e6462b;
  --red-deep:#d93d24;
  --orange:#f4a14a;
  --peach:#f6b27a;
  --cream:#fffaf0;
  --yellow:#fcd46a;
  --white:#ffffff;
}
*{box-sizing:border-box;margin:0;padding:0}
html,body{width:1200px;height:1000px;overflow:hidden}
body{background:var(--page);font-family:'Raleway',sans-serif;position:relative;color:var(--ink)}
.board-header{position:absolute;left:0;top:0;width:1200px;height:56px;background:linear-gradient(var(--bar-top),var(--bar-bottom));box-shadow:0 2px 4px rgba(0,0,0,.18)}
.board-title{position:absolute;left:28px;top:15px;font-weight:800;font-size:22px;letter-spacing:.3px}
.board-label{position:absolute;right:28px;top:14px;font-size:24px;font-weight:400}
.card{position:absolute;top:115px;width:536px;height:754px;overflow:hidden;box-shadow:0 1px 5px rgba(0,0,0,.25);
  background:linear-gradient(180deg,var(--cream) 0%,#fff1c8 50%,var(--yellow) 100%)}
.card--front{left:47px}
.card--back{left:613px;width:535px}
.card svg.art{position:absolute;left:0;top:0}
.abs{position:absolute}
.brand{font-weight:700;font-size:19px;line-height:20px;color:var(--red);text-align:center}
.headline-light{font-weight:300;font-size:40px;color:var(--red);letter-spacing:.5px;white-space:nowrap}
.headline-bold{font-weight:800;font-size:51px;color:var(--red);white-space:nowrap}
.rule{height:3px;background:var(--red)}
.intro{font-size:14px;line-height:17.5px;color:var(--red);text-align:justify}
.offer-band{left:0;top:606px;width:536px;height:40px;background:var(--red);color:var(--white);font-size:19px;font-weight:500;text-align:center;line-height:40px;letter-spacing:.3px}
.price{top:650px;height:47px;line-height:47px;font-size:29px;text-align:center}
.price b{font-weight:800}
.price--weekday{left:0;width:269px;background:var(--red-deep);color:var(--white)}
.price--weekend{left:269px;width:240px;background:var(--white);color:var(--red)}
.footer-line{top:720px;font-size:13px;color:var(--red)}
.location{font-size:14px;color:var(--red)}
.back-title{font-size:35px;font-weight:300;color:var(--red);white-space:nowrap}
.back-title b{font-weight:800}
.back-intro{font-size:11.6px;line-height:13.4px;color:var(--red);text-align:justify}
.step{position:absolute;left:149px;width:347px}
.step h3{font-size:14px;font-weight:700;color:var(--red);line-height:16px}
.step p{font-size:11.2px;line-height:13px;color:var(--red);text-align:justify}
.social{font-size:12px;color:var(--red);left:69px}
.caption{position:absolute;top:908px;font-size:23px;font-weight:400;width:300px;text-align:center}
</style>
</head>
<body>
<header class="board-header">
  <div class="board-title">BRINDLE OAK ACCUPUNCTURE</div>
  <div class="board-label">Card Design</div>
</header>

<!-- FRONT -->
<section class="card card--front">
  <svg class="art" width="536" height="754" viewBox="0 0 536 754">
    <defs>
      <linearGradient id="collage" x1="0" y1="0" x2="1" y2="1">
        <stop offset="0" stop-color="#fbe6cf"/><stop offset=".5" stop-color="#f3b070"/><stop offset="1" stop-color="#c97f44"/>
      </linearGradient>
      <linearGradient id="portrait" x1="0" y1="0" x2="0" y2="1">
        <stop offset="0" stop-color="#f2e4d6"/><stop offset=".45" stop-color="#c99a82"/><stop offset="1" stop-color="#6f3f63"/>
      </linearGradient>
    </defs>
    <g role="img" aria-label="Collage photo: acupuncture needles placed on a relaxed client's face, a smiling family and a happy older couple">
      <path d="M0 0H536V275C450 280 380 285 330 292C260 300 220 330 190 355C140 320 80 300 0 290Z" fill="url(#collage)"/>
      <path d="M110 180C200 120 320 130 400 170L400 292C330 292 250 310 190 355C160 300 130 250 110 180Z" fill="#f6a955" opacity=".55"/>
      <path d="M250 0H370C330 40 300 80 290 130C270 90 260 40 250 0Z" fill="#fde2a8" opacity=".7"/>
    </g>
    <g role="img" aria-label="Portrait photo of a smiling acupuncture practitioner">
      <path d="M323 0H536V272C470 276 400 282 323 290Z" fill="url(#portrait)"/>
    </g>
  </svg>

  <div class="abs brand" style="left:355px;top:340px;width:165px">Brindle Oak<br>Accupuncture</div>

  <div class="abs headline-light" style="left:43px;top:393px">ALWAYS WANT TO TRY</div>
  <div class="abs headline-bold" style="left:40px;top:428px">ACUPUNCTURE?</div>
  <div class="abs rule" style="left:41px;top:487px;width:455px"></div>
  <p class="abs intro" style="left:41px;top:503px;width:455px">Acupuncture originates from China and has been practiced there for thousands of years. Although there are records of acupuncture being used hundreds of years ago in Europe, it was during the second half of the twentieth century it began to spread rapidly in Western Europe, the United States and Canada.</p>

  <div class="abs offer-band">TRY 3 ACUPUNCTURE SESSIONS FROM US FOR ONLY</div>
  <div class="abs price price--weekday">weekdays <b>£30</b></div>
  <div class="abs price price--weekend">weekends <b>£35</b></div>

  <div class="abs footer-line" style="left:28px">www.brindleoakclinic.com</div>
  <div class="abs footer-line" style="right:24px">Tel No.: (02) 555 018 2046</div>
</section>

<!-- BACK -->
<section class="card card--back">
  <svg class="art" width="535" height="754" viewBox="0 0 535 754">
    <defs>
      <linearGradient id="relax" x1="0" y1="0" x2="1" y2="0">
        <stop offset="0" stop-color="#f7d9bd"/><stop offset=".6" stop-color="#f0c3a0"/><stop offset="1" stop-color="#b78660"/>
      </linearGradient>
      <radialGradient id="skin1"><stop offset="0" stop-color="#f3c9c4"/><stop offset="1" stop-color="#d98f8c"/></radialGradient>
      <radialGradient id="skin2"><stop offset="0" stop-color="#f3d6bf"/><stop offset="1" stop-color="#c99572"/></radialGradient>
      <radialGradient id="skin3"><stop offset="0" stop-color="#f1c9a6"/><stop offset="1" stop-color="#c58a5c"/></radialGradient>
      <radialGradient id="skin4"><stop offset="0" stop-color="#f4e6dc"/><stop offset="1" stop-color="#b9a69a"/></radialGradient>
    </defs>
    <rect width="535" height="180" fill="#ffffff"/>
    <path d="M0 180V0H535V180C420 150 260 175 0 180Z" fill="#ffffff"/>
    <path d="M0 0H400C340 20 320 60 330 125C250 60 130 45 0 55Z" fill="var(--orange)" opacity=".85"/>
    <path d="M0 55C130 45 250 60 330 125C250 85 130 75 0 80Z" fill="#fbcf8a" opacity=".8"/>
    <path d="M535 0V115C470 110 410 115 360 130C390 70 430 25 470 0Z" fill="var(--peach)"/>
    <g role="img" aria-label="Close-up photo of skin after cupping treatment"><circle cx="88" cy="295" r="46" fill="url(#skin1)" stroke="#fff" stroke-width="3"/></g>
    <g role="img" aria-label="Photo of hands taking a pulse at the wrist"><circle cx="88" cy="393" r="46" fill="url(#skin2)" stroke="#fff" stroke-width="3"/></g>
    <g role="img" aria-label="Photo of acupuncture needles placed on a back"><circle cx="88" cy="493" r="46" fill="url(#skin3)" stroke="#fff" stroke-width="3"/></g>
    <g role="img" aria-label="Photo of a smiling older woman"><circle cx="88" cy="593" r="46" fill="url(#skin4)" stroke="#fff" stroke-width="3"/></g>
    <g role="img" aria-label="Photo of a smiling woman relaxing during acupuncture treatment">
      <path d="M192 730C230 690 300 640 380 610C430 592 470 590 535 588V730Z" fill="url(#relax)"/>
    </g>
    <rect x="0" y="730" width="535" height="24" fill="#ffffff"/>
    <path d="M44 83a10 10 0 0 1 20 0c0 8-10 18-10 18s-10-10-10-18z" fill="var(--red)"/>
    <circle cx="54" cy="83" r="4" fill="#ffffff"/>
    <circle cx="51" cy="682" r="9" fill="var(--red)"/>
    <circle cx="51" cy="707" r="9" fill="var(--red)"/>
  </svg>

  <div class="abs brand" style="left:298px;top:47px;width:165px">Brindle Oak<br>Accupuncture</div>
  <div class="abs location" style="left:74px;top:89px">Fernvale, IA 50999</div>

  <div class="abs back-title" style="left:43px;top:133px">WHAT IS <b>ACUPUNCTURE?</b></div>
  <div class="abs rule" style="left:42px;top:176px;width:453px;height:2px"></div>
  <p class="abs back-intro" style="left:42px;top:182px;width:453px">A key component of Traditional Chinese medicine, acupuncture is most commonly used to treat pain. Traditional Chinese medicine explains acupuncture as a technique for balancing the flow of energy or life force — known as qi or chi (CHEE) — believed to flow through pathways (meridians) in your body.</p>

  <div class="step" style="top:254px"><h3>Painful Back</h3><p>Lorem ipsum dolor sit amet, consectetur adipiscing elit, sed do eiusmod tempor incididunt ut labore et dolore magna aliqua. Ut enim ad minim veniam, quis nostrud exercitation ullamco laboris nisi ut aliquip ex ea commodo consequat. Duis aute irure dolor in reprehenderit.</p></div>
  <div class="step" style="top:348px"><h3>Pulse Taking</h3><p>Lorem ipsum dolor sit amet, consectetur adipiscing elit, sed do eiusmod tempor incididunt ut labore et dolore magna aliqua. Ut enim ad minim veniam, quis nostrud exercitation ullamco laboris nisi ut aliquip ex ea commodo consequat. Duis aute irure dolor in reprehenderit.</p></div>
  <div class="step" style="top:453px"><h3>Treatment</h3><p>Lorem ipsum dolor sit amet, consectetur adipiscing elit, sed do eiusmod tempor incididunt ut labore et dolore magna aliqua. Ut enim ad minim veniam, quis nostrud exercitation ullamco laboris nisi ut aliquip ex ea commodo consequat. Duis aute irure dolor in reprehenderit.</p></div>
  <div class="step" style="top:552px;width:300px"><h3>Result: Happy Life!</h3><p style="text-align:left">Lorem ipsum dolor sit amet, consectetur adipiscing elit, sed do eius mod tempor incididunt ut labore et dolore magna aliqua. Ut enim ad minim veniam, quis nostrud exercitation ullamco laboris nisi ut aliquip ex ea commodo consequat exercitation liyup.</p></div>

  <div class="abs social" style="top:675px">@brindleoakclinic</div>
  <div class="abs social" style="top:700px">brindleoakclinic</div>
</section>

<div class="caption" style="left:165px">Front Design</div>
<div class="caption" style="left:730px">Back Design</div>
</body>
</html>
```